Geschäftspapiere Campingplatz
Zielgruppe
Campingplatz
Aufgabenstellung
Geschäftspapiere, Briefpapier, Visitenkarte, Briefumschlag und DIN A5 Memoblock farblich und designmäßig am Logo orientiert.
Memoblock sollte sich vom Briefpapier unterscheiden und nicht so viele Daten enthalten.
Website, E-Mail, Telefonnummer, Festnetz, Adresse und Inhaber sollen auf dem Briefpapier erscheinen.
Auf der Visitenkarte soll nur statt Inhaber stehen und zusätzlich die Handynummer, sowie alle anderen Daten.
Die Datensätze sollten sich mit entsprechendem Programm von uns bearbeiten lassen.

```html
<!DOCTYPE html>
<html lang="de">
<head>
<meta charset="utf-8">
<title>Camping Wiesental – Geschäftspapiere</title>
<link href="https://fonts.googleapis.com/css2?family=Lato:wght@300;400;700&display=swap" rel="stylesheet">
<style>
  :root {
    --backdrop: #2c3e56;
    --paper: #f7f7f5;
    --green: #86a556;
    --green-dark: #6f8d42;
    --ink: #2d2d2d;
    --grey: #8a8a8a;
    --white: #ffffff;
    --dash: #c9d7b3;
  }
  * { margin: 0; padding: 0; box-sizing: border-box; }
  html, body { width: 1200px; height: 800px; overflow: hidden; }
  body {
    background: var(--backdrop);
    font-family: "Lato", sans-serif;
    position: relative;
  }

  /* Memo pad */
  .memo-pad {
    position: absolute; left: 40px; top: 60px;
    width: 520px; height: 640px;
    background: var(--paper);
    display: flex; flex-direction: column; justify-content: flex-end;
  }
  .memo-pad__footer {
    background: var(--green);
    color: var(--white);
    padding: 26px 30px;
    font-size: 17px; line-height: 1.55; font-weight: 400;
  }
  .memo-pad__footer .gap { height: 14px; }

  /* Business cards */
  .card {
    position: absolute; left: 680px;
    width: 460px; height: 297px;
    background: var(--paper);
    overflow: hidden;
  }
  .card--front { top: 60px; display: flex; align-items: center; justify-content: center; }
  .brand { display: flex; align-items: center; gap: 12px; }
  .brand__dot { width: 16px; height: 16px; border-radius: 50%; background: var(--green); }
  .brand__name { font-size: 38px; font-weight: 700; color: var(--green); letter-spacing: 0.5px; }

  .card--back { top: 420px; }
  .card__head { height: 82px; padding-top: 16px; text-align: center; }
  .card__holder { font-size: 32px; line-height: 1; letter-spacing: 1px; }
  .card__holder-prefix { font-weight: 300; color: var(--green); }
  .card__holder-name { font-weight: 400; color: var(--ink); }
  .card__company { font-size: 13px; font-weight: 300; color: var(--grey); letter-spacing: 1.5px; margin-top: 2px; }

  .card__band {
    position: absolute; left: 0; right: 0; top: 82px; height: 195px;
    background: var(--green);
    display: grid; grid-template-columns: repeat(3, 1fr);
    padding: 18px 10px 0;
  }
  .contact { display: flex; flex-direction: column; align-items: center; color: var(--white); text-align: center; }
  .contact__icon { width: 78px; height: 78px; margin-bottom: 12px; }
  .contact__text { font-size: 11.5px; line-height: 1.45; }
</style>
</head>
<body>

  <section class="memo-pad">
    <div class="memo-pad__footer">
      <p>info@camping-wiesental.de</p>
      <div class="gap"></div>
      <p>www.camping-wiesental.de</p>
      <p>Telefon: +49 12345678</p>
      <p>Telefax: +49 1234567890</p>
    </div>
  </section>

  <section class="card card--front">
    <div class="brand">
      <span class="brand__dot"></span>
      <span class="brand__name">Camping Wiesental</span>
    </div>
  </section>

  <section class="card card--back">
    <header class="card__head">
      <p class="card__holder"><span class="card__holder-prefix">FAM.</span> <span class="card__holder-name">BERGER</span></p>
      <p class="card__company">CAMPING WIESENTAL</p>
    </header>

    <div class="card__band">
      <div class="contact contact--address">
        <svg class="contact__icon" viewBox="0 0 80 80" aria-hidden="true">
          <circle cx="40" cy="40" r="37" fill="none" stroke="var(--dash)" stroke-width="1.5" stroke-dasharray="5 4"/>
          <path d="M40 25c-6 0-10 4.5-10 10 0 7 10 18 10 18s10-11 10-18c0-5.5-4-10-10-10z" fill="var(--white)"/>
          <circle cx="40" cy="35" r="3.8" fill="var(--green)"/>
        </svg>
        <p class="contact__text">Wiesengrund 12<br>54321 Talbach</p>
      </div>

      <div class="contact contact--phone">
        <svg class="contact__icon" viewBox="0 0 80 80" aria-hidden="true">
          <circle cx="40" cy="40" r="37" fill="none" stroke="var(--dash)" stroke-width="1.5" stroke-dasharray="5 4"/>
          <path d="M26 36c0-5 6-8 14-8s14 3 14 8v2h-7v-3h-14v3h-7z" fill="var(--white)"/>
          <path d="M33 39h14l5 12H28z" fill="var(--white)"/>
          <g fill="var(--green)">
            <rect x="35" y="42" width="2.5" height="2" /><rect x="39" y="42" width="2.5" height="2" /><rect x="43" y="42" width="2.5" height="2" />
            <rect x="35" y="46" width="2.5" height="2" /><rect x="39" y="46" width="2.5" height="2" /><rect x="43" y="46" width="2.5" height="2" />
          </g>
        </svg>
        <p class="contact__text">+49 123 / 45 67 8<br>Timo: xxxxxxx<br>Harald: xxxxxxx</p>
      </div>

      <div class="contact contact--web">
        <svg class="contact__icon" viewBox="0 0 80 80" aria-hidden="true">
          <circle cx="40" cy="40" r="37" fill="none" stroke="var(--dash)" stroke-width="1.5" stroke-dasharray="5 4"/>
          <g fill="none" stroke="var(--white)" stroke-width="2.2">
            <circle cx="40" cy="40" r="12"/>
            <ellipse cx="40" cy="40" rx="5.5" ry="12"/>
            <line x1="28" y1="40" x2="52" y2="40"/>
            <line x1="30" y1="33" x2="50" y2="33"/>
            <line x1="30" y1="47" x2="50" y2="47"/>
          </g>
        </svg>
        <p class="contact__text">info@camping-wiesental.de<br>www.camping-wiesental.de</p>
      </div>
    </div>
  </section>

</body>
</html>
```